Vordaline - Fitness Coach. Needs a Business Card Design that I can also use for other advertising

Established 2012, I have finished the KTRB National Certificate in Fitness & Personal Training. Harlow Cross First Aid Certificate. I have the Auckland 800m track records for MW45. I also came 1st at the 2012 Pellamar Games in 800 & 1500m. I am passionate about health & fitness and would like to help people reach their health & fitness goals. I also take health & fitness weekends. Main interests - Running, Weight Training, Yoga & Aqua Jogging. I like strength/power, but am femine.

Target Market(s)

Male or Female 18 and over that wants to improve their health & fitness

Industry/Entity Type

Advertising

Requirements
Must have
• my name: Rosalind K Tarbury contact details: ros@quillsend.co.nz mobile - 021 583917 URL name: linkvane.com/rosalindKtarbury - VordaLine
Photo of Me

```html
<!DOCTYPE html>
<html lang="en">
<head>
<meta charset="utf-8">
<title>VordaLine – Rosalind K Tarbury, Fitness Coach</title>
<link rel="stylesheet" href="https://fonts.googleapis.com/css2?family=Arimo:wght@400;700&display=swap">
<style>
  :root {
    --paper: #ffffff;
    --pattern: #eceef0;
    --brand-blue: #4d80d8;
    --contact-blue: #6b90e0;
    --slate: #5f8099;
    --coral: #e07262;
    --ink: #1a1a1a;
    --icon-blue: #3d8fd8;
    --photo-top: #f08a4a;
    --photo-bottom: #4a4f57;
  }
  * { margin: 0; padding: 0; box-sizing: border-box; }
  html, body { width: 1200px; height: 777px; overflow: hidden; background: var(--paper); }
  .card {
    position: relative; width: 1200px; height: 777px; overflow: hidden;
    background: var(--paper);
    font-family: "Arimo", Arial, sans-serif;
  }
  .exercise-pattern {
    position: absolute; inset: 0;
    background: radial-gradient(ellipse at 60% 45%, var(--paper) 0%, var(--pattern) 85%);
    opacity: .8;
  }
  .brand {
    position: absolute; left: 114px; top: 80px;
    font-size: 82px; font-weight: 700; letter-spacing: 3px;
    color: var(--brand-blue); line-height: 1;
  }
  .tagline {
    position: absolute; left: 114px; top: 182px;
    font-size: 38px; font-weight: 400; letter-spacing: 3.2px; color: var(--slate); line-height: 1;
  }
  .tagline .amp { color: var(--coral); }
  .coach-name {
    position: absolute; left: 192px; top: 335px;
    font-size: 72px; font-weight: 400; letter-spacing: 2px; color: var(--coral); line-height: 1;
    white-space: nowrap;
  }
  .coach-role {
    position: absolute; left: 342px; top: 404px;
    font-size: 57px; font-weight: 400; letter-spacing: 3px; color: var(--slate); line-height: 1;
  }
  .contact-heading {
    position: absolute; left: 114px; top: 556px;
    font-size: 41px; font-weight: 400; letter-spacing: 2px; color: var(--contact-blue); line-height: 1;
  }
  .contact-list { position: absolute; left: 56px; top: 604px; list-style: none; }
  .contact-list li {
    display: flex; align-items: center; height: 54px;
    font-size: 42px; font-weight: 400; letter-spacing: 3px; color: var(--ink);
    white-space: nowrap;
  }
  .contact-list svg { width: 40px; height: 40px; margin-right: 18px; flex: none; }
  .coach-photo {
    position: absolute; left: 912px; top: 54px; width: 262px; height: 582px;
    border-radius: 120px 120px 40px 40px;
    background: linear-gradient(180deg, var(--photo-top) 0%, var(--photo-top) 45%, var(--photo-bottom) 100%);
    opacity: .85;
  }
</style>
</head>
<body>
<main class="card">
  <div class="exercise-pattern" role="img" aria-label="Faint grey pattern of exercising figure silhouettes"></div>

  <h1 class="brand">VordaLine</h1>
  <p class="tagline">meeting your health <span class="amp">&amp;</span> fitness goals</p>

  <div class="coach-photo" role="img" aria-label="Photo of the fitness coach jumping with a raised fist, in an orange top and dark leggings"></div>

  <h2 class="coach-name">Rosalind K Tarbury</h2>
  <p class="coach-role">Fitness Coach</p>

  <p class="contact-heading">Contact:</p>
  <ul class="contact-list">
    <li>
      <svg viewBox="0 0 40 40" aria-hidden="true">
        <circle cx="20" cy="20" r="18" fill="var(--icon-blue)"/>
        <path d="M12 17c0-3 3-5 8-5s8 2 8 5v2h-4v-2h-8v2h-4z M13 21h14l2 8H11z" fill="#fff"/>
      </svg>
      mobile - 021 583 917
    </li>
    <li>
      <svg viewBox="0 0 40 40" aria-hidden="true">
        <circle cx="20" cy="20" r="18" fill="var(--icon-blue)"/>
        <rect x="10" y="13" width="20" height="14" rx="1.5" fill="#fff"/>
        <path d="M10 14l10 8 10-8" fill="none" stroke="var(--icon-blue)" stroke-width="2"/>
      </svg>
      ros@quillsend.co.nz
    </li>
    <li>
      <svg viewBox="0 0 40 40" aria-hidden="true">
        <rect x="3" y="3" width="34" height="34" rx="8" fill="var(--icon-blue)"/>
      </svg>
      linkvane.com/rosalindKtarbury - VordaLine
    </li>
  </ul>
</main>
</body>
</html>
```